Logo & Graphic Design for Children's Event

We need help designing the logo and marketing materials for our summer children's event "Star Parade". This program is for children ages 5-10 and should have a bold, fun feel to it. I would like a strong logo that is the primary feature of the design with additional supporting artwork elements that can be used flexibly in a variety of formats and mediums. I would like the design to capture the overall feel of the event. This event will be themed like a TV game show/variety show and should reflect this vibe.

This design will be used for outside marketing and branding and needs to be provided in a vector format. The types of mediums it would be used on is yard signs, banners, door hangers, social media, etc. (Samples of materials from previous events included in the uploaded files to help you get a feel for the quality and tone that we aim for with this event.)

Target Market(s)

Families with children ages 5-10

Industry/Entity Type

Church

Requirements
Must have
• - Strong logo that communicates the feel of the event and includes the name "Star Parade". - Flexible supporting artwork elements that can be used in a variety of mediums. - Must use fonts that are available from free, open sources or can be provided upon delivery of completed project. - Must be kid and family friendly - Event date June 10-14 must be included - Event time 6:30-8:30pm included - Include our church logo attached - Event web address Brightpathhollow.com/KDC
Nice to have
• - A themed background that could be adapted for use on powerpoint.
Should not have
• - Any content that is scary, violent or not suitable for an audience of children.

```html
<!DOCTYPE html>
<html lang="en">
<head>
<meta charset="utf-8">
<title>Star Parade – Summer Kids Event</title>
<link rel="stylesheet" href="https://fonts.googleapis.com/css2?family=Cinzel:wght@600&family=Luckiest+Guy&family=Marcellus&display=swap">
<style>
  :root {
    --paper: #ffffff;
    --ink: #111111;
    --muted: #3f3f3f;
    --sky: #5b9bd5;
    --cherry: #ee4444;
    --bubblegum: #dd6fae;
    --sunshine: #fbbf1a;
    --outline: #fff200;
    --cyan: #00aeef;
    --lime: #8dc63f;
    --red: #ed1c24;
    --orange: #f7941d;
    --purple: #662d91;
    --magenta: #d81b60;
    --green: #00a651;
    --indigo: #2e3192;
    --planet-sea: #3f7fc1;
    --planet-land: #2dba86;
  }
  * { box-sizing: border-box; margin: 0; padding: 0; }
  html, body { width: 1200px; height: 1200px; overflow: hidden; background: var(--paper); }
  .poster { position: relative; width: 1200px; height: 1200px; overflow: hidden; background: var(--paper); }

  .shape { position: absolute; z-index: 0; }
  .blob-sky { left: 310px; top: -40px; width: 500px; height: 110px; background: var(--sky); border-radius: 0 0 60% 50% / 0 0 100% 100%; }
  .blob-sun { left: 1036px; top: -110px; width: 260px; height: 252px; background: var(--cherry); border-radius: 50%; }
  .blob-pink { left: -60px; top: 328px; width: 180px; height: 368px; background: var(--bubblegum); border-radius: 55% 45% 60% 40% / 30% 40% 60% 70%; }
  .stroke-yellow { left: 1118px; top: 200px; width: 56px; height: 236px; background: linear-gradient(160deg, #fcd34d, var(--sunshine)); border-radius: 40px 30px 30px 40px; transform: rotate(18deg); }
  .art-rocket { left: 34px; top: 50px; width: 120px; height: 200px; background: linear-gradient(150deg, #3f7fc1 0%, #3f7fc1 55%, #f5c518 80%, #ee4444 100%); border-radius: 60px 60px 30px 30px; transform: rotate(30deg); }
  .art-planet { left: 1042px; top: 574px; width: 200px; height: 196px; border-radius: 50%; background: radial-gradient(circle at 40% 40%, var(--planet-land), var(--planet-sea) 70%); }
  .art-girl { left: 0; top: 740px; width: 220px; height: 380px; background: linear-gradient(180deg, #f7a825 0%, #fbd85a 35%, #dd6fae 75%, #f6c7a8 100%); border-radius: 40% 40% 30% 30%; }
  .art-boy { left: 952px; top: 772px; width: 248px; height: 316px; background: linear-gradient(180deg, #2dba86 0%, #f7c21a 35%, #f7941d 60%, #3f7fc1 85%); border-radius: 40% 40% 30% 30%; }

  .title { position: absolute; left: 0; width: 1200px; text-align: center; font-family: "Luckiest Guy", "Arial Black", sans-serif; line-height: 1; z-index: 1; }
  .title-top { top: 108px; font-size: 250px; letter-spacing: 4px; -webkit-text-stroke: 10px var(--outline); paint-order: stroke fill; }
  .title-bottom { top: 372px; font-size: 220px; text-shadow: 14px 14px 0 var(--ink); }
  .c-cyan { color: var(--cyan); } .c-lime { color: var(--lime); } .c-red { color: var(--red); } .c-orange { color: var(--orange); }
  .c-purple { color: var(--purple); } .c-magenta { color: var(--magenta); } .c-green { color: var(--green); } .c-indigo { color: var(--indigo); } .c-cyan2 { color: var(--cyan); }

  .details { position: absolute; left: 0; width: 1200px; text-align: center; font-family: "Cinzel", Georgia, serif; font-weight: 600; color: var(--ink); white-space: nowrap; z-index: 1; }
  .tagline { top: 690px; font-size: 38px; letter-spacing: 4px; }
  .date { top: 762px; font-size: 28px; letter-spacing: 13px; }
  .time { top: 834px; font-size: 28px; letter-spacing: 13px; }

  .church { position: absolute; left: 410px; top: 912px; display: flex; align-items: center; gap: 8px; z-index: 1; }
  .church-dot { width: 114px; height: 114px; border-radius: 50%; background: var(--ink); }
  .church-name { font-family: "Cinzel", Georgia, serif; font-weight: 600; font-size: 25px; line-height: 1.1; color: var(--ink); white-space: nowrap; }

  .web { position: absolute; left: 0; top: 1050px; width: 1200px; text-align: center; font-family: "Marcellus", Georgia, serif; font-size: 40px; color: var(--ink); text-transform: uppercase; white-space: nowrap; z-index: 1; }
  .contact { position: absolute; left: 0; top: 1128px; width: 1200px; display: flex; justify-content: center; gap: 22px; font-family: "Marcellus", Georgia, serif; font-size: 19px; color: var(--muted); text-transform: uppercase; white-space: nowrap; z-index: 1; }
  .contact .sep { color: var(--muted); }
</style>
</head>
<body>
<main class="poster">
  <div class="shape blob-sky"></div>
  <div class="shape blob-sun"></div>
  <div class="shape blob-pink"></div>
  <div class="shape stroke-yellow" role="img" aria-label="Yellow painted brush stroke"></div>
  <div class="shape art-rocket" role="img" aria-label="Cartoon rocket ship flying upward"></div>
  <div class="shape art-planet" role="img" aria-label="Cartoon planet Earth"></div>
  <div class="shape art-girl" role="img" aria-label="Cartoon girl with a crown jumping with joy"></div>
  <div class="shape art-boy" role="img" aria-label="Cartoon boy in a unicorn hood jumping with joy"></div>

  <h1>
    <span class="title title-top"><span class="c-cyan">S</span><span class="c-lime">T</span><span class="c-red">A</span><span class="c-orange">R</span></span>
    <span class="title title-bottom"><span class="c-purple">P</span><span class="c-magenta">A</span><span class="c-green">R</span><span class="c-indigo">A</span><span class="c-orange">D</span><span class="c-cyan2">E</span></span>
  </h1>

  <p class="details tagline">MARK YOUR SUMMER CALENDARS</p>
  <p class="details date">DATE: JUNE 10-14</p>
  <p class="details time">EVENT TIME: 6:30-8:30PM</p>

  <div class="church">
    <div class="church-dot"></div>
    <div class="church-name">BRIGHT PATH<br>COMMUNITY CHURCH</div>
  </div>

  <p class="web">Brightpathhollow.com/KDC</p>
  <p class="contact">
    <span>info@brightpathhollow.com</span><span class="sep">|</span>
    <span>555-014-2290</span><span class="sep">|</span>
    <span>1450 Meadow Ln. Hollow Springs KS, 66000</span>
  </p>
</main>
</body>
</html>
```